Innovative Industrial Technology Start up need complete branding solution!

Corvana88 are a specialist industrial Technology solution provider offering End to End Control Systems, Electrical, Industrial IT and Communications services to the Energy, Resources and Infrastructure sectors.

Our ethos is to nurture and deliver creative, innovative and sustainable industrial technology solutions through the use of latest technologies and cutting edge industry practices. Our approach is progressive and personal, balancing wider project economics between return on investment and process metrics to promote value and positive returns to our clients.

We are looking for a contemporary, fresh, edgy and captivating brand. Simple and effective as well as scale-able. The brand should reflect our progressive approach to project delivery while representing a youthful yet professional image. Bold Colours, strong fonts along with clean lines for any logos.

We are looking for the following deliverables:
1) Corporate brand and style guide
2) Business Cards
3) Letterhead
4) Formatted word document (including cover page\table of contents\tables\appendix)
5) Email Signature
6) Capability Statement (Outline only - Text can be provided)

A Sample document is provided from a similar organisation for information.

Target Market(s)

Energy, Resources, Infrastructure

Industry/Entity Type

Progressive

Logo Text

Corvana88

Logo styles of interest
Abstract Logo
Wordmark Logo
Lettermark Logo
Font styles to use
Serif
Sans Serif

```html
<!DOCTYPE html>
<html lang="en">
<head>
<meta charset="utf-8">
<title>Corvana88 Business Card</title>
<link rel="stylesheet" href="https://fonts.googleapis.com/css2?family=Montserrat:ital,wght@0,300;0,600;1,300&display=swap">
<style>
  :root {
    --paper: #ffffff;
    --ink: #141414;
    --accent: #7b1c1f;
  }
  html, body {
    margin: 0;
    padding: 0;
    width: 1200px;
    height: 720px;
    overflow: hidden;
    background: var(--paper);
  }
  .card {
    position: relative;
    width: 1200px;
    height: 720px;
    background: var(--paper);
    font-family: "Montserrat", sans-serif;
    color: var(--ink);
  }
  .card-frame {
    position: absolute;
    left: 0;
    top: 0;
  }
  .person-name {
    position: absolute;
    left: 137px;
    top: 123px;
    margin: 0;
    font-size: 49px;
    font-weight: 600;
    line-height: 1;
  }
  .person-title {
    position: absolute;
    left: 137px;
    top: 184px;
    margin: 0;
    font-size: 50px;
    font-weight: 300;
    font-style: italic;
    line-height: 1;
  }
  .contact-list {
    position: absolute;
    left: 135px;
    top: 285px;
    margin: 0;
    font-size: 50px;
    font-weight: 300;
    line-height: 64px;
    letter-spacing: 0;
  }
  .contact-list span {
    display: block;
  }
  .website {
    position: absolute;
    left: 321px;
    top: 499px;
    width: 519px;
    height: 74px;
    display: flex;
    align-items: center;
    justify-content: center;
    font-size: 41px;
    font-weight: 600;
    letter-spacing: 0.3px;
  }
</style>
</head>
<body>
  <main class="card">
    <svg class="card-frame" width="1200" height="720" viewBox="0 0 1200 720" aria-hidden="true">
      <polyline points="137,261 1031,261 1031,573 840,573" fill="none" stroke="var(--accent)" stroke-width="4"/>
      <rect x="321" y="499" width="519" height="74" fill="none" stroke="var(--accent)" stroke-width="4"/>
    </svg>

    <h1 class="person-name">Name</h1>
    <p class="person-title">Title</p>

    <p class="contact-list">
      <span class="contact-phone">1.555.204.3189</span>
      <span class="contact-email">Name@corvana88.com</span>
    </p>

    <div class="website">www.corvana88.com</div>
  </main>
</body>
</html>
```